Dating Coach needs a Book Cover Design

My new book called "When to Turn the Tide: Meeting Romance Among the Endless Crowd of Digital Courtship" needs a cover! I tried to make one on my own, but it's just not my skill set :) Please see attached for my best attempt. I'd like to see the title smaller and the tagline bigger - so that the tagline is easier to read. But I'm not sure how to do this and still have the Title look great. I'm also considering if the "TURN THE TIDE" part should not be in all caps. Looking forward to your ideas! I'm also afraid that the drawing is a bit too cartoonish and doesn't match my brand. I'm looking for something elegant and also very approachable and down to earth. My website is www.petrawendtcoaching.example so you can use as reference! Please see my attached brand style guide for colors. This will be an e-book that I give away for free to anyone who signs up for my newsletter. Some mock-ups would also be great to use in advertising.

```html
<!DOCTYPE html>
<html lang="en">
<head>
<meta charset="UTF-8">
<title>When to Turn the Tide — Book Cover</title>
<link rel="stylesheet" href="https://fonts.googleapis.com/css2?family=Cormorant+Garamond:wght@500;600&display=swap">
<style>
  :root {
    --cover-plum: #6c507e;
    --cover-plum-deep: #5f4671;
    --ink-cream: #f2e8d8;
    --rule-cream: rgba(242, 232, 216, 0.55);
    --accent-gold: #c9a45a;
  }
  * { margin: 0; padding: 0; box-sizing: border-box; }
  html, body {
    width: 960px;
    height: 1200px;
    overflow: hidden;
    background: var(--cover-plum);
  }
  .book-cover {
    position: relative;
    width: 960px;
    height: 1200px;
    background: linear-gradient(180deg, var(--cover-plum) 0%, var(--cover-plum-deep) 100%);
    color: var(--ink-cream);
    font-family: "Cormorant Garamond", Georgia, serif;
    text-align: center;
  }
  .title-lead {
    position: absolute;
    top: 78px;
    left: 0;
    right: 0;
    font-size: 58px;
    font-weight: 500;
    letter-spacing: 1px;
  }
  .title-main {
    position: absolute;
    top: 150px;
    left: 0;
    right: 0;
    font-size: 150px;
    font-weight: 500;
    line-height: 142px;
    letter-spacing: 1px;
  }
  .title-divider {
    position: absolute;
    top: 432px;
    left: 140px;
    right: 140px;
    height: 30px;
    display: flex;
    align-items: center;
    gap: 18px;
  }
  .title-divider .rule {
    flex: 1;
    height: 1.5px;
    background: var(--rule-cream);
  }
  .title-divider svg { width: 30px; height: 28px; }
  .subtitle {
    position: absolute;
    top: 490px;
    left: 80px;
    right: 80px;
    font-size: 46px;
    font-weight: 500;
    line-height: 58px;
    letter-spacing: 3px;
  }
  .cover-illustration {
    position: absolute;
    top: 690px;
    left: 130px;
    width: 700px;
    height: 330px;
    border-radius: 4px;
    background: radial-gradient(ellipse at 50% 65%, rgba(242, 232, 216, 0.55) 0%, rgba(242, 232, 216, 0.22) 45%, rgba(242, 232, 216, 0) 75%);
  }
  .author-name {
    position: absolute;
    top: 1082px;
    left: 0;
    right: 0;
    font-size: 48px;
    font-weight: 600;
    letter-spacing: 6px;
    text-transform: uppercase;
  }
</style>
</head>
<body>
  <main class="book-cover">
    <p class="title-lead">When to</p>
    <h1 class="title-main">Turn the<br>Tide</h1>

    <div class="title-divider">
      <span class="rule"></span>
      <svg viewBox="0 0 30 28" aria-hidden="true">
        <path d="M15 25 C6 18 2 13 2 8.5 C2 5 4.8 2.5 8 2.5 C11 2.5 13.5 4.5 15 7 C16.5 4.5 19 2.5 22 2.5 C25.2 2.5 28 5 28 8.5 C28 13 24 18 15 25 Z" fill="none" stroke="var(--accent-gold)" stroke-width="1.8"/>
      </svg>
      <span class="rule"></span>
    </div>

    <p class="subtitle">Meeting Romance Among the<br>Endless Crowd of<br>Digital Courtship</p>

    <div class="cover-illustration" role="img" aria-label="Cover illustration area in cream linework"></div>

    <p class="author-name">Petra Wendt</p>
  </main>
</body>
</html>
```